KELPO's Coffee Liqueur Shot Arabica

Need a lable for a 500ml bottle of homemade Coffee liqueur.
Name:
KELPO's
Coffee
Shot

Shape: Round, 80mm
Color of the lable should be black and letters in black.
Letters KELPO's min 12mm hight.
Color of the liqueur is dark brown.
Add: 500ml
Add: 38% vol.
Should have a bean on the lable.
Maybe some bullet words on the bottom...
Prefered design see Pic1a with bottle.

Target Market(s)

People that enjoy coffee in shots, in coctails, with ice or on top of icecream or any other dessert

Font styles to use
Serif

Colors

Designer to choose colors to be used in the design.

Requirements
Must have
• See Pic 1a
Nice to have
• See Pic1a (bottle)
Should not have
• Different colors

```html
<!DOCTYPE html>
<html lang="en">
<head>
<meta charset="utf-8">
<title>KELPO's Coffee Shot – Label</title>
<link rel="stylesheet" href="https://fonts.googleapis.com/css2?family=Ultra&family=Abril+Fatface&family=Bungee&family=Playfair+Display:wght@700;900&display=swap">
<style>
  :root {
    --backdrop: #cdb597;
    --label-black: #0d0d0d;
    --label-ink: #f4f2ee;
    --band-light: #e9e9e7;
    --band-shade: #c9c9c6;
    --art-mid: #8d8b87;
    --art-dark: #3a3937;
  }
  html, body {
    margin: 0;
    padding: 0;
    width: 1200px;
    height: 720px;
    overflow: hidden;
    background: var(--backdrop);
  }
  .canvas {
    position: relative;
    width: 1200px;
    height: 720px;
  }
  .label { display: block; }
  .label-face { fill: var(--label-black); }
  .scallop-line { fill: none; stroke: var(--label-ink); stroke-width: 3; }
  .scallop-bumps { fill: none; stroke: var(--label-ink); stroke-width: 9; stroke-linecap: round; stroke-dasharray: 0 13.4; }
  .arc-title {
    font-family: "Abril Fatface", serif;
    font-size: 46px;
    fill: var(--label-ink);
    letter-spacing: 3px;
  }
  .name-band { fill: url(#bandShade); }
  .brand-name {
    font-family: "Ultra", serif;
    font-size: 84px;
    fill: var(--label-black);
    letter-spacing: 1px;
  }
  .art-area { fill: url(#artShade); }
  .badge { fill: var(--label-ink); }
  .badge-text {
    font-family: "Playfair Display", serif;
    font-weight: 900;
    fill: var(--label-black);
  }
  .arc-small {
    font-family: "Playfair Display", serif;
    font-weight: 700;
    font-size: 15px;
    fill: var(--label-ink);
    letter-spacing: 2px;
  }
  .rule { stroke: var(--label-ink); stroke-width: 1.5; }
  .variety {
    font-family: "Ultra", serif;
    fill: var(--label-ink);
  }
  .arc-bottom {
    font-family: "Bungee", sans-serif;
    font-size: 38px;
    fill: var(--label-ink);
    letter-spacing: 14px;
  }
</style>
</head>
<body>
<main class="canvas">
  <svg class="label" width="1200" height="720" viewBox="0 0 1200 720" aria-label="KELPO's Coffee Shot round label">
    <defs>
      <linearGradient id="bandShade" x1="0" y1="0" x2="0" y2="1">
        <stop offset="0" stop-color="var(--band-light)"/>
        <stop offset="1" stop-color="var(--band-shade)"/>
      </linearGradient>
      <radialGradient id="artShade">
        <stop offset="0" stop-color="var(--art-mid)"/>
        <stop offset="1" stop-color="var(--art-dark)"/>
      </radialGradient>
      <clipPath id="ringClip"><circle cx="0" cy="0" r="284"/></clipPath>
      <path id="titleArc" d="M -232,0 A 232 232 0 0 1 232,0"/>
      <path id="bottomArc" d="M -250,0 A 250 250 0 0 0 250,0"/>
      <path id="spiritArc" d="M -206,45 A 56 56 0 0 1 -94,45"/>
    </defs>

    <g transform="translate(600 360)">
      <circle class="label-face" r="330"/>
      <circle class="scallop-line" r="288"/>
      <circle class="scallop-bumps" r="292"/>

      <text class="arc-title"><textPath href="#titleArc" startOffset="50%" text-anchor="middle">Coffee Shot</textPath></text>

      <rect class="art-area" x="-45" y="-225" width="90" height="70" rx="10" role="img" aria-label="Engraved coffee plant sprout"/>

      <g clip-path="url(#ringClip)">
        <polygon class="name-band" points="-300,-148 -220,-150 -120,-146 0,-150 120,-147 220,-150 300,-148 300,-66 200,-64 80,-68 -40,-64 -160,-67 -300,-65"/>
      </g>
      <text class="brand-name" x="0" y="-74" text-anchor="middle">KELPO's</text>

      <rect class="art-area" x="-20" y="-62" width="40" height="50" rx="8" role="img" aria-label="Engraved coffee plant stem"/>
      <rect class="art-area" x="-75" y="-10" width="150" height="84" rx="18" role="img" aria-label="Engraved sack of coffee beans with two large beans"/>
      <rect class="art-area" x="95" y="-8" width="115" height="62" rx="28" role="img" aria-label="Engraved pair of coffee beans"/>

      <circle class="badge" cx="-150" cy="45" r="32"/>
      <text class="badge-text" x="-150" y="45" text-anchor="middle" font-size="18">38%</text>
      <text class="badge-text" x="-150" y="62" text-anchor="middle" font-size="12">VL</text>
      <text class="arc-small"><textPath href="#spiritArc" startOffset="50%" text-anchor="middle">HANDCRAFT SPIRIT</textPath></text>

      <circle class="badge" cx="140" cy="-45" r="28"/>
      <text class="badge-text" x="140" y="-45" text-anchor="middle" font-size="14">500</text>
      <text class="badge-text" x="140" y="-30" text-anchor="middle" font-size="10">ml</text>

      <line class="rule" x1="-120" y1="82" x2="120" y2="82"/>
      <text class="variety" x="0" y="125" text-anchor="middle" font-size="38">ARABIKA</text>
      <text class="variety" x="0" y="146" text-anchor="middle" font-size="15">BEANS</text>

      <text class="arc-bottom"><textPath href="#bottomArc" startOffset="50%" text-anchor="middle">COFFEE LIQUEUR</textPath></text>
    </g>
  </svg>
</main>
</body>
</html>
```